Label for high-end indie coffee package

I need a label for high-end indie coffee package.

Coffee comes from Mt. Elgon, Trans-Nzoia County, Kenya. The coffee will be sold in Finland. The package as such will be semi matte black and the label will be printed out as a sticker.

Maximum measurements for the label would around 9 x 9 centimeters. It can be a square / rectangle / circle. I would like it to include influences from coffee origins (Kenya) and also demonstrate the high-end quality of the coffee with the modern twist.

The label should include the following text:

Coffee Name:
Morelu Vintaro AA
Washed & Natural

Origins:
Mt. Elgon, Trans-Nzoia County, Kenya

Growing altitude:
Altitude: 1 800 amsl

Coffee variety:
100 % Arabica

Following fields should be possible to be filled afterwards when the need occurs:
roast date
best before
roasted by

I'll be more than happy to answer any questions!

Finland. High-end customers, design coffee shops.

```html
<!DOCTYPE html>
<html lang="en">
<head>
<meta charset="utf-8">
<title>Morelu Vintaro AA – Coffee Label</title>
<link rel="stylesheet" href="https://fonts.googleapis.com/css2?family=Roboto:wght@400;500&display=swap">
<style>
  :root {
    --backdrop: #161616;
    --label-paper: #ffffff;
    --title-brown: #4a2c26;
    --ink: #2b2b2b;
    --rule: #3a3a3a;
    --fill-line: #8a8a8a;
  }
  html, body {
    margin: 0;
    width: 1200px;
    height: 1200px;
    overflow: hidden;
    background: var(--backdrop);
  }
  .canvas {
    position: relative;
    width: 1200px;
    height: 1200px;
  }
  .label {
    position: absolute;
    left: 150px;
    top: 126px;
    width: 900px;
    height: 947px;
    font-family: "Roboto", Arial, sans-serif;
  }
  .label-shape {
    position: absolute;
    inset: 0;
  }
  .coffee-name {
    position: absolute;
    left: 0;
    width: 100%;
    top: 122px;
    margin: 0;
    text-align: center;
    color: var(--title-brown);
    font-weight: 500;
    font-size: 88px;
    line-height: 80px;
    letter-spacing: 1px;
  }
  .process {
    position: absolute;
    left: 0;
    width: 100%;
    top: 305px;
    margin: 0;
    text-align: center;
    color: var(--ink);
    font-size: 31px;
    letter-spacing: 1px;
  }
  .spec {
    position: absolute;
    left: 52px;
    margin: 0;
    color: var(--ink);
  }
  .spec-term {
    display: block;
    font-size: 28px;
    letter-spacing: 0.5px;
    margin-bottom: 12px;
  }
  .spec-value {
    display: block;
    margin: 0;
    font-size: 19px;
    line-height: 27px;
  }
  .spec-origins { top: 410px; }
  .spec-altitude { top: 586px; }
  .spec-variety { top: 746px; }

  .roast-fields {
    position: absolute;
    left: 52px;
    top: 838px;
    width: 392px;
    margin: 0;
    color: var(--ink);
  }
  .roast-field {
    display: flex;
    align-items: flex-end;
    height: 26px;
    margin-bottom: 4px;
  }
  .roast-field dt {
    font-size: 15px;
    letter-spacing: 0.5px;
    white-space: nowrap;
    margin-right: 10px;
  }
  .roast-field dd {
    flex: 1;
    margin: 0 0 4px;
    border-bottom: 1.5px solid var(--fill-line);
  }
</style>
</head>
<body>
<div class="canvas">
  <section class="label">
    <svg class="label-shape" width="900" height="947" viewBox="0 0 900 947" xmlns="http://www.w3.org/2000/svg">
      <defs>
        <pattern id="teeth-top" x="0" y="0" width="20" height="24" patternUnits="userSpaceOnUse">
          <path d="M0 24 L10 0 L20 24 Z" fill="#ffffff"/>
        </pattern>
        <pattern id="teeth-bottom" x="0" y="923" width="20" height="24" patternUnits="userSpaceOnUse">
          <path d="M0 0 L10 24 L20 0 Z" fill="#ffffff"/>
        </pattern>
        <linearGradient id="bean-tone" x1="0" y1="0" x2="1" y2="1">
          <stop offset="0" stop-color="#e9ddd3"/>
          <stop offset="1" stop-color="#cdb7a6"/>
        </linearGradient>
      </defs>
      <rect x="0" y="0" width="900" height="24" fill="url(#teeth-top)"/>
      <rect x="0" y="23" width="900" height="901" fill="#ffffff"/>
      <rect x="0" y="923" width="900" height="24" fill="url(#teeth-bottom)"/>

      <g class="spec-table" fill="none" stroke="#3a3a3a" stroke-width="2">
        <polyline points="20,926 20,367 883,367 883,926"/>
        <line x1="473" y1="367" x2="474" y2="926"/>
        <line x1="20" y1="562" x2="473" y2="566"/>
        <line x1="20" y1="727" x2="473" y2="730"/>
        <line x1="20" y1="822" x2="473" y2="824"/>
      </g>

      <rect x="530" y="440" width="310" height="420" rx="40" fill="url(#bean-tone)"
            role="img" aria-label="Engraved sketch of six roasted coffee beans"/>
    </svg>

    <h1 class="coffee-name">MORELU<br>VINTARO AA</h1>
    <p class="process">WASHED &amp; NATURAL</p>

    <dl class="spec spec-origins">
      <dt class="spec-term">ORIGINS:</dt>
      <dd class="spec-value">Mt. Elgon,<br>Trans-Nzoia County, Kenya</dd>
    </dl>
    <dl class="spec spec-altitude">
      <dt class="spec-term">GROWING ALTITUDE:</dt>
      <dd class="spec-value">Altitude: 1 800 amsl</dd>
    </dl>
    <dl class="spec spec-variety">
      <dt class="spec-term">COFFEE VARIETY:</dt>
      <dd class="spec-value">100 % Arabica</dd>
    </dl>

    <dl class="roast-fields">
      <div class="roast-field"><dt>ROAST DATE:</dt><dd></dd></div>
      <div class="roast-field"><dt>BEST BEFORE:</dt><dd></dd></div>
      <div class="roast-field"><dt>ROASTED BY:</dt><dd></dd></div>
    </dl>
  </section>
</div>
</body>
</html>
```